Building company buisness cards

We are looking for a sharp modern new look for our business cards.
We are a New Zealand based company that specialises in house and land packages.
We have attached a photo of the current logo and would like to see if it can be improved somehow if needed.
We are open to any colours but we have chosen green at this stage.
Feel free to change the font and make the logo smarter looking.
Play with the colours and see what looks best.

We want a card that looks so good know one will want to throw it away!

Target Market(s)

Home buyers

Industry/Entity Type

Building

Contact Information for Business Card

Dorian Keswick
0217392604
dkeswick@tidewellhomecraft.co.nz
tidewellhomecraft.co.nz

Font styles to use
Serif
Sans Serif

Colors

Designer to choose colors to be used in the design.

Requirements
Must have
• Logo and company name on one side, details on the other side
Nice to have
• Color codes for the original green are HEX #4a8028, RGB(74,128,40), CMYK(42,0,69,50)
• Round corners, Raised and/or spot UV

```html
<!DOCTYPE html>
<html lang="en">
<head>
<meta charset="utf-8">
<title>Tidewell Homecraft – Business Cards</title>
<link rel="stylesheet" href="https://fonts.googleapis.com/css2?family=Montserrat:wght@600;800&family=Lato:wght@400&display=swap">
<style>
  :root {
    --page: #ececec;
    --green: #8dc21f;
    --grey: #747474;
    --grey-dark: #5e5e5e;
    --paper: #ffffff;
    --text: #6a6a6a;
    --faint: #e6e6e6;
  }
  * { box-sizing: border-box; margin: 0; padding: 0; }
  html, body { width: 1200px; height: 1021px; overflow: hidden; }
  body { background: var(--page); position: relative; font-family: "Lato", sans-serif; }

  .card {
    position: absolute;
    left: 250px;
    width: 700px;
    height: 400px;
    border-radius: 22px;
    overflow: hidden;
    box-shadow: 0 6px 18px rgba(0,0,0,.18);
  }

  /* Logo side */
  .card--brand { top: 50px; background: var(--grey); }
  .brand-pattern {
    position: absolute; inset: 0;
    background: linear-gradient(135deg, #8a8a8a 0%, var(--grey) 50%, var(--grey-dark) 100%);
  }
  .brand-lockup {
    position: absolute; left: 0; right: 0; top: 170px;
    display: flex; align-items: center; justify-content: center; gap: 14px;
  }
  .brand-mark { width: 26px; height: 26px; background: var(--green); flex: none; }
  .brand-name {
    font-family: "Montserrat", sans-serif; font-weight: 800;
    font-size: 44px; color: var(--green); letter-spacing: -0.5px;
    white-space: nowrap;
  }

  /* Details side */
  .card--details { top: 540px; background: var(--paper); }
  .side-band { position: absolute; inset: 0; }
  .details-watermark {
    position: absolute; right: 24px; bottom: 0;
    width: 220px; height: 230px;
    background: linear-gradient(180deg, var(--faint) 0%, #eeeeee 100%);
    border-radius: 12px 12px 0 0;
  }
  .details-lockup {
    position: absolute; left: 150px; top: 52px;
    display: flex; align-items: center; gap: 12px;
  }
  .details-lockup .brand-mark { width: 20px; height: 20px; }
  .details-lockup .brand-name { font-size: 38px; }

  .person { position: absolute; left: 170px; top: 170px; }
  .person-name {
    font-family: "Montserrat", sans-serif; font-weight: 600;
    font-size: 26px; color: var(--green); white-space: nowrap;
  }
  .person-role { font-size: 17px; color: var(--text); margin-top: 2px; }

  .contact { position: absolute; left: 150px; top: 268px; list-style: none; }
  .contact li { font-size: 19px; color: var(--text); line-height: 27px; white-space: nowrap; }

  .contact-icons { position: absolute; left: 68px; top: 268px; }
</style>
</head>
<body>

<section class="card card--brand" aria-label="Logo side">
  <div class="brand-pattern" role="img" aria-label="Embossed repeating pattern of the house emblem on grey"></div>
  <div class="brand-lockup">
    <span class="brand-mark"></span>
    <span class="brand-name">tidewell homecraft</span>
  </div>
</section>

<section class="card card--details" aria-label="Details side">
  <svg class="side-band" width="700" height="400" viewBox="0 0 700 400" aria-hidden="true">
    <polygon points="0,0 120,0 120,240 96,262 96,400 0,400" fill="#747474"/>
    <polygon points="120,0 132,0 132,246 108,268 108,400 96,400 96,262 120,240" fill="#8dc21f"/>
  </svg>
  <div class="details-watermark" role="img" aria-label="Large faint house emblem"></div>

  <div class="details-lockup">
    <span class="brand-mark"></span>
    <span class="brand-name">tidewell homecraft</span>
  </div>

  <div class="person">
    <p class="person-name">Dorian Keswick</p>
    <p class="person-role">Founder</p>
  </div>

  <svg class="contact-icons" width="20" height="81" viewBox="0 0 20 81" aria-hidden="true" fill="none" stroke="#ffffff" stroke-width="1.6">
    <path d="M5 5 q-3 2 0 8 q4 6 9 7 q3 0 3-3 l-3-2 -2 2 q-3-1-4-4 l2-2 -2-4z" fill="#ffffff" stroke="none"/>
    <rect x="2" y="34" width="16" height="11" rx="1"/>
    <path d="M2 34 l8 6 8-6"/>
    <circle cx="10" cy="67" r="8"/>
    <path d="M2 67 h16 M10 59 q-5 8 0 16 M10 59 q5 8 0 16"/>
  </svg>
  <ul class="contact">
    <li>0217392604</li>
    <li>dkeswick@tidewellhomecraft.co.nz</li>
    <li>tidewellhomecraft.co.nz</li>
  </ul>
</section>

</body>
</html>
```